Red Mesa Brazilian Jiu Jitsu Ad

We need an advertisement we can use for multiple sources including printed ads and digital media. We would like our ad to provide potential students with information about our mission and services. We are a martial arts studio in Sagebrook, NM who specialize in Brazilian Jiu Jitsu and Muay Thai.

We train our students in Brazilian Jiu Jitsu & Muay Thai for self defense
purposes as well as for sport. No matter your preference, we can help you reach your martial arts goals.

The final product should reflect our services, goals, and provide contact information.

```html
<!DOCTYPE html>
<html lang="en">
<head>
<meta charset="utf-8">
<title>Red Mesa Brazilian Jiu Jitsu Ad</title>
<link rel="stylesheet" href="https://fonts.googleapis.com/css2?family=Oswald:wght@500;600&display=swap">
<style>
  :root {
    --backdrop: #e8e8e8;
    --ink-dark: #222226;
    --brand-red: #e0121b;
    --white: #ffffff;
    --wall: #ead7cf;
    --mat-red: #d9412a;
    --mat-blue: #2a4fa8;
    --badge: #e9e9ea;
  }
  * { margin: 0; padding: 0; box-sizing: border-box; }
  html, body { width: 1200px; height: 983px; overflow: hidden; background: var(--backdrop); }
  body { position: relative; font-family: "Oswald", "Arial Narrow", sans-serif; text-transform: uppercase; }

  .flyer {
    position: absolute; width: 477px; height: 617px; overflow: hidden;
    box-shadow: 2px 3px 6px rgba(0,0,0,.18);
  }
  .flyer--v { left: 88px; top: 73px; }
  .flyer--diagonal { left: 621px; top: 232px; }

  .photo {
    position: absolute; inset: 0;
    background: linear-gradient(180deg, var(--wall) 0%, var(--wall) 30%, #c99a86 45%, var(--mat-red) 62%, #8a3a55 80%, var(--mat-blue) 100%);
  }
  .shapes { position: absolute; inset: 0; width: 100%; height: 100%; }

  .brand-mark { position: absolute; display: flex; align-items: center; justify-content: center; border-radius: 50%; background: var(--badge); box-shadow: 0 0 0 3px rgba(255,255,255,.6); }
  .brand-mark__name { width: 80%; text-align: center; font-weight: 600; font-size: 11px; line-height: 1.15; color: var(--ink-dark); }

  .headline { position: absolute; color: var(--brand-red); font-weight: 600; font-size: 24px; line-height: 31px; letter-spacing: -.2px; white-space: nowrap; }
  .intro { position: absolute; color: var(--white); font-weight: 500; font-size: 15.5px; line-height: 20.5px; letter-spacing: -.5px; white-space: nowrap; }
  .cta { position: absolute; color: var(--white); font-weight: 500; white-space: nowrap; }
  .cta__title { font-size: 21px; line-height: 26px; }
  .cta__line { font-size: 15.5px; line-height: 20px; }
  .contact { position: absolute; color: var(--brand-red); font-weight: 500; font-size: 15.5px; line-height: 21px; }

  .flyer--v .headline { left: 37px; top: 134px; }
  .flyer--v .intro { left: 84px; top: 200px; }
  .flyer--v .cta { left: 183px; top: 264px; }
  .flyer--v .brand-mark { left: 190px; top: 16px; width: 102px; height: 102px; }

  .flyer--diagonal .headline { left: 20px; top: 22px; }
  .flyer--diagonal .intro { left: 20px; top: 97px; }
  .flyer--diagonal .contact { left: 20px; top: 178px; }
  .flyer--diagonal .brand-mark { left: 325px; top: 286px; width: 102px; height: 102px; }
  .flyer--diagonal .cta { left: 328px; top: 437px; }
  .flyer--diagonal .cta__title { font-size: 24px; line-height: 30px; }
  .flyer--diagonal .cta__line { font-size: 17px; line-height: 23px; }
</style>
</head>
<body>

<section class="flyer flyer--v">
  <div class="photo" role="img" aria-label="Students training jiu jitsu and kicking heavy bags on red and blue gym mats"></div>
  <svg class="shapes" viewBox="0 0 477 617" aria-hidden="true">
    <polygon points="0,132 376,132 477,221 477,235 427,235 232,359 50,235 0,235" fill="var(--ink-dark)" opacity=".93"/>
    <polyline points="0,235 50,235 238,617" fill="none" stroke="var(--white)" stroke-width="4"/>
    <polyline points="477,235 427,235 242,617" fill="none" stroke="var(--white)" stroke-width="4"/>
  </svg>
  <div class="brand-mark"><span class="brand-mark__name">Red Mesa Brazilian Jiu Jitsu</span></div>
  <h1 class="headline">We can help you reach<br>your martial arts goals.</h1>
  <p class="intro">We are a martial arts studio in Sagebrook,<br>NM who specialize in Brazilian Jiu Jitsu and<br>Muay Thai.</p>
  <div class="cta">
    <p class="cta__title">Call today</p>
    <p class="cta__line">+000 000 000</p>
    <p class="cta__line">mail@web.com</p>
  </div>
</section>

<section class="flyer flyer--diagonal">
  <div class="photo" role="img" aria-label="Jiu jitsu instructor drilling a takedown while a student kicks a heavy bag"></div>
  <svg class="shapes" viewBox="0 0 477 617" aria-hidden="true">
    <polygon points="429,0 477,0 477,68" fill="var(--brand-red)"/>
    <polygon points="0,0 297,0 364,130 0,269" fill="var(--ink-dark)" opacity=".93"/>
    <line x1="38" y1="255" x2="214" y2="421" stroke="var(--brand-red)" stroke-width="3"/>
    <polygon points="214,421 477,421 477,617 408,617" fill="var(--brand-red)" opacity=".95"/>
  </svg>
  <h1 class="headline">We can help you reach<br>your martial arts goals.</h1>
  <p class="intro">We are a martial arts studio in Sage-<br>brook, NM who specialize in Brazilian Jiu<br>Jitsu and Muay Thai.</p>
  <div class="contact">
    <p>+000 000 000</p>
    <p>mail@web.com</p>
  </div>
  <div class="brand-mark"><span class="brand-mark__name">Red Mesa Brazilian Jiu Jitsu</span></div>
  <div class="cta">
    <p class="cta__title">Call today</p>
    <p class="cta__line">+000 000 000</p>
    <p class="cta__line">mail@web.com</p>
  </div>
</section>

</body>
</html>
```